Business Card Design Project

Business Card
We are rebranding with a new logo
Industry/Entity Type
Business
Contact Information for Business Card
Dennis Marlow +61 427581962 dennis@qovo.com.au P.O. Box 872 Kelvindale QLD 4309
Requirements
Must have
- Logo

```html
<!DOCTYPE html>
<html lang="en">
<head>
<meta charset="utf-8">
<title>Qovo International — Business Card</title>
<link rel="stylesheet" href="https://fonts.googleapis.com/css2?family=Poppins:wght@400;500;600&display=swap">
<style>
  :root {
    --backdrop: #e6e6e6;
    --card-white: #ffffff;
    --brand-orange: #f0821e;
    --brand-blue: #0a86b4;
    --brand-navy: #0b5f86;
    --strip-black: #141414;
    --text-light: #ffffff;
  }
  * { margin: 0; padding: 0; box-sizing: border-box; }
  html, body {
    width: 1200px;
    height: 1200px;
    overflow: hidden;
    background: var(--backdrop);
    font-family: "Poppins", sans-serif;
  }
  .canvas {
    width: 1200px;
    height: 1200px;
    display: flex;
    align-items: center;
    justify-content: center;
  }
  .business-card {
    position: relative;
    width: 1000px;
    height: 560px;
    background: var(--card-white);
    overflow: hidden;
    box-shadow: 0 18px 40px rgba(0,0,0,0.18);
  }
  .card-waves {
    position: absolute;
    inset: 0;
    width: 100%;
    height: 100%;
  }
  .company-name {
    position: absolute;
    left: 78px;
    top: 92px;
    color: var(--brand-navy);
    font-size: 48px;
    font-weight: 600;
    line-height: 1;
    letter-spacing: 0.5px;
  }
  .holder-name {
    position: absolute;
    right: 70px;
    top: 372px;
    color: var(--text-light);
    font-size: 44px;
    font-weight: 500;
    letter-spacing: 3px;
    line-height: 1.1;
    text-transform: uppercase;
  }
  .contact-strip {
    position: absolute;
    left: 0;
    right: 0;
    bottom: 0;
    height: 80px;
    background: var(--strip-black);
    display: flex;
    align-items: center;
    justify-content: space-between;
    padding: 0 36px;
    color: var(--text-light);
    font-size: 19px;
    font-weight: 400;
    letter-spacing: 0.5px;
    white-space: nowrap;
  }
  .contact-item {
    display: flex;
    align-items: center;
    gap: 14px;
  }
  .contact-icon {
    width: 32px;
    height: 32px;
    flex: none;
  }
</style>
</head>
<body>
<main class="canvas">
  <article class="business-card">
    <svg class="card-waves" viewBox="0 0 1000 560" aria-hidden="true">
      <path d="M0 322 C 360 330, 610 150, 1000 128 L1000 480 L0 480 Z" fill="var(--brand-orange)"/>
      <path d="M0 370 C 360 372, 620 205, 1000 190 L1000 480 L0 480 Z" fill="var(--brand-blue)"/>
    </svg>

    <p class="company-name">Qovo International</p>

    <h1 class="holder-name">Dennis Marlow</h1>

    <footer class="contact-strip">
      <div class="contact-item">
        <svg class="contact-icon" viewBox="0 0 32 32" aria-hidden="true">
          <circle cx="16" cy="16" r="14" fill="none" stroke="#fff" stroke-width="2"/>
          <path d="M11 9 l3 0 l1.5 4 l-2 1.5 a9 9 0 0 0 4 4 l1.5 -2 l4 1.5 l0 3 a2 2 0 0 1 -2 2 a13 13 0 0 1 -12 -12 a2 2 0 0 1 2 -2 z" fill="#fff"/>
        </svg>
        <span>+61 427581962</span>
      </div>
      <div class="contact-item">
        <svg class="contact-icon" viewBox="0 0 32 32" aria-hidden="true">
          <circle cx="16" cy="16" r="14" fill="none" stroke="#fff" stroke-width="2"/>
          <circle cx="16" cy="16" r="3.5" fill="none" stroke="#fff" stroke-width="2"/>
          <path d="M19.5 16 v1.5 a2.5 2.5 0 0 0 5 0 v-1.5 a8.5 8.5 0 1 0 -3.5 6.9" fill="none" stroke="#fff" stroke-width="2"/>
        </svg>
        <span>dennis@qovo.com.au</span>
      </div>
      <div class="contact-item">
        <svg class="contact-icon" viewBox="0 0 32 32" aria-hidden="true">
          <circle cx="16" cy="16" r="14" fill="none" stroke="#fff" stroke-width="2"/>
          <path d="M16 8 a6 6 0 0 1 6 6 c0 4.5 -6 10 -6 10 s-6 -5.5 -6 -10 a6 6 0 0 1 6 -6 z" fill="#fff"/>
          <circle cx="16" cy="14" r="2.2" fill="var(--strip-black)"/>
        </svg>
        <span>P.O. Box 872 Kelvindale QLD 4309</span>
      </div>
    </footer>
  </article>
</main>
</body>
</html>
```